Our architectural studio needs a new business card

We need a business card design for our studio based in Waterloo in Belgium. We are active in architecture, design and installation.
Our works are contemporary and minimalist. our clients are refined and cultured.
Our business card must be minimalist and refined.

Project Deadline Extended
Reason: Some designers have accepted my invitation but they don't have all replied. I want to give them a chance to make one proposal. Paul

Target Market(s)

architecture

Industry/Entity Type

Business

Contact Information for Business Card

studio: paul dornevaux studio
paul dornevaux, architecte
M. +32 471 586 927
F. +322 619 4850
www.pauldornevaux-example.com
paul@pauldornevaux-example.com
14 rue des Marronniers
1420 Waterloo
Belgium

Font styles to use
Sans Serif

Requirements
Must have
• simple, minimalist, clear, elegant and chic! Black and white
Nice to have
• embossed logo, other format like a square for example
Should not have
• color, fantasy, curves, ...

```html
<!DOCTYPE html>
<html lang="fr">
<head>
<meta charset="utf-8">
<title>Paul Dornevaux Studio — Carte de visite</title>
<link rel="stylesheet" href="https://fonts.googleapis.com/css2?family=Lato:wght@300;400;700&display=swap">
<style>
  :root {
    --backdrop: #e9e7e4;
    --card-black: #0b0b0b;
    --card-white: #ffffff;
    --ink-light: #f2f2f2;
    --ink-dark: #1a1a1a;
    --ink-muted: #4a4a4a;
    --shadow: rgba(0, 0, 0, 0.18);
  }
  * { box-sizing: border-box; margin: 0; padding: 0; }
  html, body {
    width: 1200px;
    height: 913px;
    overflow: hidden;
    background: var(--backdrop);
    font-family: "Lato", Helvetica, Arial, sans-serif;
  }
  .canvas {
    position: relative;
    width: 1200px;
    height: 913px;
  }
  .card {
    position: absolute;
    top: 313px;
    width: 500px;
    height: 286px;
    border-radius: 18px;
    box-shadow: 0 10px 30px var(--shadow);
  }
  .card--front {
    left: 70px;
    background: var(--card-black);
    color: var(--ink-light);
    display: flex;
    flex-direction: column;
    align-items: center;
    justify-content: center;
    gap: 22px;
  }
  .studio-mark {
    display: flex;
    align-items: center;
    gap: 14px;
    font-weight: 400;
    font-size: 22px;
    letter-spacing: 0.32em;
    text-transform: uppercase;
  }
  .studio-mark__square {
    width: 14px;
    height: 14px;
    background: var(--ink-light);
  }
  .card--back {
    left: 630px;
    background: var(--card-white);
    color: var(--ink-dark);
    padding: 0 0 30px 34px;
    display: flex;
    flex-direction: column;
    justify-content: flex-end;
  }
  .contact__studio {
    font-weight: 700;
    font-size: 15px;
    line-height: 1.15;
  }
  .contact__role {
    font-weight: 400;
    font-size: 12px;
    color: var(--ink-muted);
    margin-bottom: 16px;
  }
  .contact__address {
    font-style: normal;
    font-weight: 400;
    font-size: 12px;
    line-height: 1.35;
    color: var(--ink-muted);
    margin-bottom: 14px;
  }
  .contact__lines {
    list-style: none;
    font-size: 12px;
    line-height: 1.35;
    color: var(--ink-muted);
  }
  .contact__label {
    display: inline-block;
    width: 36px;
    font-weight: 700;
    color: var(--ink-dark);
  }
</style>
</head>
<body>
<main class="canvas">
  <section class="card card--front" aria-label="Recto">
    <p class="studio-mark"><span class="studio-mark__square"></span>Paul Dornevaux Studio</p>
  </section>

  <section class="card card--back" aria-label="Verso">
    <p class="contact__studio">Paul Dornevaux Studio</p>
    <p class="contact__role">Architecte</p>
    <address class="contact__address">
      14 rue des Marronniers 1420<br>
      Waterloo Belgium
    </address>
    <ul class="contact__lines">
      <li><span class="contact__label">(M) :</span>+32 471 586 927</li>
      <li><span class="contact__label">(F) :</span>+322 619 4850</li>
      <li><span class="contact__label">(E) :</span>www.pauldornevaux-example.com</li>
      <li><span class="contact__label">(W):</span>paul@pauldornevaux-example.com</li>
    </ul>
  </section>
</main>
</body>
</html>
```